Resposive web site in 4 languages + image gallery + logo design

We need a web page, which will work on all devices.
I have uploaded web page concept.
Company name: Valqueno
Industry/Entity Type
It Company
Logo Text
quality matters
Coding
Coded - Design and coding required
Number of Pages Required
1 page

```html
<!DOCTYPE html>
<html lang="en">
<head>
<meta charset="utf-8">
<title>Valqueno — Woodworks</title>
<link rel="stylesheet" href="https://fonts.googleapis.com/css2?family=Montserrat:wght@400;500;600;700;800&display=swap">
<style>
  :root {
    --ink: #111111;
    --text: #555555;
    --white: #ffffff;
    --hero-dark: #2a1d14;
    --hero-mid: #6b4a30;
    --hero-light: #a88058;
    --band: rgba(30, 24, 20, 0.82);
    --orange-1: #f7a531;
    --orange-2: #ea8a12;
    --lang-grey: #bdb6ae;
    --footer-grey: #e9e9e9;
    --thumb-line: #cfcfcf;
  }
  * { margin: 0; padding: 0; box-sizing: border-box; }
  html, body { width: 1200px; height: 1200px; overflow: hidden; background: var(--white); }
  body { font-family: "Montserrat", sans-serif; color: var(--ink); }
  .stage { position: relative; width: 1500px; height: 1500px; transform: scale(0.8); transform-origin: 0 0; overflow: hidden; }
  .abs { position: absolute; }

  /* Hero */
  .hero { left: 0; top: 0; width: 1189px; height: 618px;
    background: radial-gradient(ellipse at 55% 45%, var(--hero-light) 0%, var(--hero-mid) 35%, var(--hero-dark) 80%); }
  .logo { left: 157px; top: 26px; font-size: 28px; font-weight: 600; color: var(--white); letter-spacing: 0.5px; }
  .nav a { position: absolute; top: 35px; font-size: 18px; font-weight: 500; color: var(--white); text-decoration: none; }
  .lang { top: 41px; font-size: 12px; font-weight: 600; color: var(--lang-grey); }
  .lang-divider { left: 994px; top: 20px; width: 1px; height: 60px; background: rgba(255,255,255,0.25); }
  .lang-active { left: 1007px; top: 41px; font-size: 12px; font-weight: 600; color: var(--white); border-bottom: 2px solid var(--white); padding-bottom: 2px; }
  .hero-title { left: 152px; top: 176px; font-size: 64px; font-weight: 800; color: var(--white); line-height: 1; }
  .hero-rule { left: 154px; top: 253px; width: 373px; height: 8px; background: var(--white); }
  .hero-sub { left: 152px; top: 280px; font-size: 18px; font-weight: 500; color: var(--white); }
  .estimate { left: 0; top: 425px; width: 698px; height: 97px; background: var(--band); border-radius: 0 49px 49px 0; }
  .estimate-q { left: 156px; top: 462px; font-size: 18px; font-weight: 600; color: var(--white); }
  .quote-btn { left: 495px; top: 450px; width: 175px; height: 47px; border-radius: 24px;
    background: linear-gradient(180deg, var(--orange-1), var(--orange-2));
    color: var(--white); font-size: 18px; font-weight: 700; text-align: center; line-height: 47px; }
  .dot { top: 469px; width: 17px; height: 17px; border-radius: 50%; border: 2px solid rgba(255,255,255,0.7); }
  .dot.is-active { background: rgba(255,255,255,0.85); border-color: transparent; }

  /* Sections */
  .section-bar { width: 15px; background: var(--ink); }
  .section-title { font-size: 48px; font-weight: 800; line-height: 1; }
  .section-copy { font-size: 16px; line-height: 26px; color: var(--text); }
  .checklist { font-size: 18px; font-weight: 500; }
  .check { position: absolute; display: flex; align-items: center; gap: 13px; }
  .check svg { width: 18px; height: 16px; }
  .photo { position: absolute; }

  /* Overview */
  .thumb { left: 1189px; top: 0; width: 311px; height: 830px; }
  .t-hero { left: 0; top: 0; width: 311px; height: 141px;
    background: radial-gradient(ellipse at 50% 50%, var(--hero-light), var(--hero-mid) 40%, var(--hero-dark) 85%); }
  .t-tiny { font-size: 4px; line-height: 5.5px; color: var(--text); }
  .t-h { font-size: 11px; font-weight: 700; }
  .t-bar { width: 3px; background: var(--ink); }
  .t-list { font-size: 4px; line-height: 10.5px; font-weight: 500; }
  .t-field { height: 1px; background: var(--ink); }
</style>
</head>
<body>
<div class="stage">

  <!-- Hero -->
  <div class="abs hero" role="img" aria-label="Photo of a carpenter marking a plank with a pencil and square in a workshop with wood shavings"></div>
  <div class="abs logo">Valqueno</div>
  <nav class="nav">
    <a style="left:442px">Services</a>
    <a style="left:552px">About us</a>
    <a style="left:668px">Contact</a>
  </nav>
  <div class="abs lang" style="left:888px">EST</div>
  <div class="abs lang" style="left:921px">RUS</div>
  <div class="abs lang" style="left:956px">FIN</div>
  <div class="abs lang-divider"></div>
  <div class="abs lang-active">ENG</div>
  <h1 class="abs hero-title">Woodworks</h1>
  <div class="abs hero-rule"></div>
  <p class="abs hero-sub">We provide quality millwork products, doors, windows, and entries</p>
  <div class="abs estimate"></div>
  <p class="abs estimate-q">Are you interested in an estimate?</p>
  <div class="abs quote-btn">Get a quote</div>
  <span class="abs dot is-active" style="left:948px"></span>
  <span class="abs dot" style="left:982px"></span>
  <span class="abs dot" style="left:1016px"></span>

  <!-- Woodworks -->
  <div class="abs section-bar" style="left:111px;top:699px;height:209px"></div>
  <h2 class="abs section-title" style="left:152px;top:727px">Woodworks</h2>
  <p class="abs section-copy" style="left:152px;top:800px;width:445px">Timber is, in essence, a natural and warm material. Wood is also relatively durable and easy to work with, which has made it a favourite of builders throughout history. Our goal is to offer suitable products and quality furniture with installation and after-sales service to all of our clients. In order to achieve this, we're ready to help our clients in all stages of construction from design to production and maintenance.</p>
  <div class="checklist">
    <div class="check" style="left:174px;top:1067px"><svg viewBox="0 0 18 16"><path d="M1 8.5l5 5L17 2" fill="none" stroke="#111" stroke-width="3.4"/></svg>Furniture</div>
    <div class="check" style="left:174px;top:1113px"><svg viewBox="0 0 18 16"><path d="M1 8.5l5 5L17 2" fill="none" stroke="#111" stroke-width="3.4"/></svg>Windows</div>
    <div class="check" style="left:174px;top:1159px"><svg viewBox="0 0 18 16"><path d="M1 8.5l5 5L17 2" fill="none" stroke="#111" stroke-width="3.4"/></svg>Doors</div>
    <div class="check" style="left:361px;top:1067px"><svg viewBox="0 0 18 16"><path d="M1 8.5l5 5L17 2" fill="none" stroke="#111" stroke-width="3.4"/></svg>Staircases</div>
    <div class="check" style="left:361px;top:1113px"><svg viewBox="0 0 18 16"><path d="M1 8.5l5 5L17 2" fill="none" stroke="#111" stroke-width="3.4"/></svg>Woodcarving</div>
    <div class="check" style="left:361px;top:1159px"><svg viewBox="0 0 18 16"><path d="M1 8.5l5 5L17 2" fill="none" stroke="#111" stroke-width="3.4"/></svg>Graining</div>
  </div>
  <div class="photo" style="left:639px;top:700px;width:213px;height:158px;background:linear-gradient(160deg,#6e3a22,#3a1a10)" role="img" aria-label="Dark wooden drawers with round knobs"></div>
  <div class="photo" style="left:639px;top:866px;width:213px;height:158px;background:linear-gradient(160deg,#e6c08a,#b98650)" role="img" aria-label="Light wooden cabinet drawers with brass handles"></div>
  <div class="photo" style="left:639px;top:1034px;width:213px;height:185px;background:linear-gradient(90deg,#5a2a18,#9c8a70 55%,#4a2516)" role="img" aria-label="Wood-panelled room with a window"></div>
  <div class="photo" style="left:860px;top:700px;width:213px;height:283px;background:linear-gradient(160deg,#d9a86a,#b07a40 60%,#cfe3dc)" role="img" aria-label="Wood carving in progress with a chisel"></div>
  <div class="photo" style="left:860px;top:990px;width:213px;height:229px;background:linear-gradient(150deg,#7a3a1c,#b4623a 50%,#3e1a0c)" role="img" aria-label="Curved wooden staircase"></div>

  <!-- Stoneworks -->
  <div class="photo" style="left:110px;top:1306px;width:213px;height:178px;background:linear-gradient(150deg,#8e9aa0,#5b666c)" role="img" aria-label="Grey granite paving setts"></div>
  <div class="photo" style="left:330px;top:1306px;width:213px;height:194px;background:linear-gradient(150deg,#a0603a,#6a6460 55%,#8a4a2c)" role="img" aria-label="Wall of coloured stone bricks"></div>
  <div class="photo" style="left:110px;top:1492px;width:213px;height:8px;background:#5f7a3a" role="img" aria-label="Stone garden path"></div>
  <div class="abs section-bar" style="left:592px;top:1305px;height:195px"></div>
  <h2 class="abs section-title" style="left:634px;top:1332px">Stoneworks</h2>
  <p class="abs section-copy" style="left:633px;top:1406px;width:460px">The natural stone found in the ground has been used in construction for centuries because of its durability. A structure built by a skilled craftsman from natural stone is unique, genuine, and durable, and perfect for</p>

  <!-- Page overview -->
  <div class="abs thumb">
    <div class="abs t-hero" role="img" aria-label="Workshop photo banner"></div>
    <div class="abs" style="left:54px;top:6px;font-size:6px;font-weight:600;color:#fff">Valqueno</div>
    <div class="abs" style="left:119px;top:8px;font-size:4px;color:#fff;word-spacing:8px">Services About&nbsp;us Contact</div>
    <div class="abs" style="left:222px;top:8px;font-size:3.5px;color:#ddd;word-spacing:3px">EST RUS FIN ENG</div>
    <div class="abs t-h" style="left:53px;top:41px;color:#fff;font-size:13px">Woodworks</div>
    <div class="abs" style="left:54px;top:56px;width:84px;height:2px;background:#fff"></div>
    <div class="abs" style="left:53px;top:64px;font-size:3.5px;color:#fff">We provide quality millwork products, doors, windows, and entries</div>
    <div class="abs" style="left:0;top:98px;width:170px;height:20px;background:var(--band);border-radius:0 10px 10px 0"></div>
    <div class="abs" style="left:54px;top:105px;font-size:4px;color:#fff">Are you interested in an estimate?</div>
    <div class="abs" style="left:131px;top:103px;width:40px;height:10px;border-radius:5px;background:var(--orange-1);font-size:3.5px;color:#fff;text-align:center;line-height:10px;font-weight:700">Get a quote</div>

    <div class="abs t-bar" style="left:45px;top:160px;height:45px"></div>
    <div class="abs t-h" style="left:54px;top:164px">Woodworks</div>
    <p class="abs t-tiny" style="left:54px;top:182px;width:92px">Timber is, in essence, a natural and warm material. Wood is also relatively durable and easy to work with, which has made it a favourite of builders throughout history. Our goal is to offer suitable products and quality furniture with installation and after-sales service to all of our clients.</p>
    <div class="abs t-list" style="left:58px;top:240px">✔ Furniture<br>✔ Windows<br>✔ Doors</div>
    <div class="abs t-list" style="left:102px;top:240px">✔ Staircases<br>✔ Woodcarving<br>✔ Graining</div>
    <div class="abs" style="left:164px;top:160px;width:99px;height:117px;background:linear-gradient(150deg,#6e3a22,#d9a86a 50%,#7a3a1c)" role="img" aria-label="Woodwork photo grid"></div>

    <div class="abs" style="left:44px;top:297px;width:99px;height:115px;background:linear-gradient(150deg,#8e9aa0,#a0603a 50%,#6d8a4a)" role="img" aria-label="Stonework photo grid"></div>
    <div class="abs t-bar" style="left:154px;top:297px;height:45px"></div>
    <div class="abs t-h" style="left:163px;top:302px">Stoneworks</div>
    <p class="abs t-tiny" style="left:163px;top:320px;width:100px">The natural stone found in the ground has been used in construction for centuries because of its durability. A structure built by a skilled craftsman from natural stone is unique, genuine, and durable.</p>
    <div class="abs t-list" style="left:167px;top:366px">✔ Walls<br>✔ Terraces<br>✔ Paths<br>✔ Fences</div>
    <div class="abs t-list" style="left:212px;top:366px">✔ Outdoor kitchens<br>✔ Fireplaces<br>✔ Brickworks</div>

    <div class="abs t-bar" style="left:45px;top:432px;height:45px"></div>
    <div class="abs t-h" style="left:53px;top:437px">Restoration</div>
    <p class="abs t-tiny" style="left:53px;top:455px;width:92px">It is good to see old things returning to use again and again in homes.</p>
    <div class="abs t-list" style="left:58px;top:507px">✔ Furniture<br>✔ Windows<br>✔ Doors</div>
    <div class="abs t-list" style="left:102px;top:507px">✔ Staircases<br>✔ Floors<br>✔ Special Projects</div>
    <div class="abs" style="left:164px;top:432px;width:99px;height:110px;background:linear-gradient(150deg,#c0813e,#8a5a38 50%,#d69a5a)" role="img" aria-label="Restoration photo grid"></div>

    <div class="abs" style="left:44px;top:567px;width:99px;height:69px;background:linear-gradient(150deg,#9a7a5a,#c8a880)" role="img" aria-label="Workshop video preview"></div>
    <svg class="abs" style="left:85px;top:592px" width="16" height="16" viewBox="0 0 16 16"><path d="M4 2l10 6-10 6z" fill="#fff"/></svg>
    <div class="abs t-bar" style="left:154px;top:567px;height:45px"></div>
    <div class="abs t-h" style="left:163px;top:572px">About us</div>
    <p class="abs t-tiny" style="left:163px;top:590px;width:100px">Valqueno is a company whose work covers furniture, restoration and building with natural stone and wood.<br><br>Quality matters.<br>Valqueno</p>

    <div class="abs t-bar" style="left:45px;top:665px;height:45px"></div>
    <div class="abs t-h" style="left:54px;top:669px">Contact</div>
    <div class="abs" style="left:0;top:690px;width:143px;height:100px;background:linear-gradient(150deg,#eeeeee,#dcdcdc)" role="img" aria-label="Street map with office location"></div>
    <div class="abs" style="left:56px;top:705px;width:58px;height:38px;background:#fff"></div>
    <div class="abs t-tiny" style="left:60px;top:707px;line-height:12px;color:#111">● 12 Harbour Lane<br>☎ +000 00 0000<br>✉ hello@valqueno.com</div>
    <div class="abs" style="left:114px;top:735px;width:7px;height:7px;border-radius:50%;background:var(--orange-1)"></div>
    <p class="abs t-tiny" style="left:163px;top:695px;width:70px">Please fill in the following fields if you would like a price quote</p>
    <div class="abs t-tiny" style="left:165px;top:710px">Name</div><div class="abs t-field" style="left:163px;top:716px;width:66px"></div>
    <div class="abs t-tiny" style="left:165px;top:722px">Email</div><div class="abs t-field" style="left:163px;top:728px;width:66px"></div>
    <div class="abs t-tiny" style="left:165px;top:734px">Phone</div><div class="abs t-field" style="left:163px;top:740px;width:66px"></div>
    <div class="abs" style="left:163px;top:746px;width:91px;height:27px;border:1px solid #111"></div>
    <div class="abs t-tiny" style="left:165px;top:748px">Message</div>
    <div class="abs" style="left:163px;top:777px;width:31px;height:10px;border-radius:5px;background:var(--orange-1);font-size:3.5px;color:#fff;text-align:center;line-height:10px;font-weight:700">Submit</div>

    <div class="abs" style="left:0;top:804px;width:311px;height:21px;background:var(--footer-grey)"></div>
    <div class="abs" style="left:42px;top:811px;font-size:6px;font-weight:600">Valqueno</div>
    <div class="abs" style="left:93px;top:812px;font-size:3px;word-spacing:6px">Services About&nbsp;us Contact</div>
    <div class="abs" style="left:215px;top:812px;font-size:3px;color:#888">© Valqueno. All rights reserved</div>
  </div>

</div>
</body>
</html>
```